Corporate Business Card

Very professional, Modern, Not to busy, include phone address email, website
(253) 555-0174, 61807 19th Street N, Kent, WA 98517, marcus@kestrelbayholding.com, brelvanindustries.com

Target Market(s)

Manufacturing

Industry/Entity Type

Aero, machining, manufacturing, Off road racing

Contact Information for Business Card

Phone, address email, website

```html
<!DOCTYPE html>
<html lang="en">
<head>
<meta charset="utf-8">
<title>Brelvan Industries – Business Card</title>
<link href="https://fonts.googleapis.com/css2?family=Roboto:wght@400;500;700&family=Montserrat:wght@500;800&display=swap" rel="stylesheet">
<style>
  :root{
    --bg:#2b2e33;
    --card:#ffffff;
    --navy:#1c3a8a;
    --red:#d5232b;
    --white:#ffffff;
  }
  *{box-sizing:border-box;margin:0;padding:0}
  html,body{width:1200px;height:900px;overflow:hidden;background:var(--bg)}
  body{position:relative;font-family:"Roboto",sans-serif}
  .card{
    position:absolute;top:295px;width:540px;height:309px;
    background:var(--card);border-radius:3px;
    box-shadow:0 10px 30px rgba(0,0,0,.45);overflow:hidden;
  }
  .card--back{left:40px}
  .card--front{left:620px}

  .brand{position:absolute;color:var(--navy);font-family:"Montserrat",sans-serif}
  .brand__name{font-weight:800;letter-spacing:1px;line-height:1}
  .brand__sub{font-weight:500;line-height:1;letter-spacing:1px}
  .brand__dot{display:inline-block;background:var(--red);vertical-align:middle}

  .card--back .brand{left:26px;top:24px}
  .card--back .brand__name{font-size:34px}
  .card--back .brand__sub{font-size:15px;margin-top:4px;padding-left:2px}
  .card--back .brand__dot{width:10px;height:10px;margin-left:6px}
  .card--back .rule{position:absolute;left:26px;top:92px;width:90px;height:2px;background:var(--navy)}

  .name-band{
    position:absolute;left:150px;top:100px;width:330px;height:48px;
    background:var(--navy);color:var(--white);
    clip-path:polygon(0 0,90% 0,100% 100%,0 100%);
    display:flex;align-items:center;padding-left:12px;gap:12px;
  }
  .name-band svg{width:30px;height:30px;flex:none}
  .name-band__name{font-size:21px;font-weight:700;line-height:1}
  .name-band__title{font-size:11px;font-weight:400;margin-top:3px}

  .contact{
    position:absolute;height:26px;background:var(--red);color:var(--white);
    clip-path:polygon(0 0,93% 0,100% 100%,0 100%);
    display:flex;align-items:center;gap:8px;padding-left:8px;
    font-size:12px;font-weight:400;
  }
  .contact svg{width:13px;height:13px;flex:none}
  .contact--address{left:120px;top:162px;width:340px}
  .contact--phone{left:100px;top:196px;width:340px}
  .contact--email{left:80px;top:230px;width:340px}
  .contact--web{left:60px;top:264px;width:340px}

  .card--front .brand{left:0;right:0;top:112px;text-align:center}
  .card--front .brand__name{font-size:58px}
  .card--front .brand__sub{font-size:22px;margin-top:8px}
  .card--front .brand__dot{width:14px;height:14px;margin-left:10px}
</style>
</head>
<body>
  <section class="card card--back" aria-label="Business card back">
    <div class="brand">
      <div class="brand__name">BRELVAN<span class="brand__dot"></span></div>
      <div class="brand__sub">Industries</div>
    </div>
    <div class="rule"></div>

    <div class="name-band">
      <svg viewBox="0 0 24 24" fill="#fff" aria-hidden="true"><circle cx="12" cy="7" r="4.5"/><path d="M3 22c0-5 4-8 9-8s9 3 9 8z"/></svg>
      <div>
        <div class="name-band__name">Daniel Hartwell</div>
        <div class="name-band__title">President and CEO</div>
      </div>
    </div>

    <div class="contact contact--address">
      <svg viewBox="0 0 24 24" fill="#fff" aria-hidden="true"><path d="M12 2a7 7 0 0 0-7 7c0 5 7 13 7 13s7-8 7-13a7 7 0 0 0-7-7zm0 9.5A2.5 2.5 0 1 1 12 6.5a2.5 2.5 0 0 1 0 5z"/></svg>
      <span>61807 19th Street N, Kent, WA 98517</span>
    </div>
    <div class="contact contact--phone">
      <svg viewBox="0 0 24 24" fill="#fff" aria-hidden="true"><path d="M6.6 10.8a15 15 0 0 0 6.6 6.6l2.2-2.2c.3-.3.7-.4 1-.2 1.1.4 2.3.6 3.6.6.6 0 1 .4 1 1V20c0 .6-.4 1-1 1A17 17 0 0 1 3 4c0-.6.4-1 1-1h3.5c.6 0 1 .4 1 1 0 1.3.2 2.5.6 3.6.1.3 0 .7-.2 1z"/></svg>
      <span>(253) 555-0174</span>
    </div>
    <div class="contact contact--email">
      <svg viewBox="0 0 24 24" fill="#fff" aria-hidden="true"><path d="M3 5h18v14H3z" fill="none" stroke="#fff" stroke-width="2"/><path d="M3 5l9 8 9-8" fill="none" stroke="#fff" stroke-width="2"/></svg>
      <span>marcus@kestrelbayholding.com</span>
    </div>
    <div class="contact contact--web">
      <svg viewBox="0 0 24 24" fill="none" stroke="#fff" stroke-width="2" aria-hidden="true"><circle cx="12" cy="12" r="9"/><path d="M3 12h18M12 3c3 3 3 15 0 18M12 3c-3 3-3 15 0 18"/></svg>
      <span>brelvanindustries.com</span>
    </div>
  </section>

  <section class="card card--front" aria-label="Business card front">
    <div class="brand">
      <div class="brand__name">BRELVAN<span class="brand__dot"></span></div>
      <div class="brand__sub">Industries</div>
    </div>
  </section>
</body>
</html>
```